Boutique Bed and Breakfast needs new website

we require a new website for our 11 room bed and breakfast in the heart of RIVERBEND MOAMA. Its an older style establishment and we would love the features on there to take quick fast room bookings. Please check out our current website www.harrowgatelodge.com.au We also require it to be ZPhone friendly

Target Market(s)

Travellers, corporates accommodation industry

Industry/Entity Type

Accommodation

Number of Pages Required

5+ page

Font styles to use
Sans Serif
Decorative
Script

Colors
86cfc6
33b8a4
00a990
85cae6
ecf7fb
cee9f5
fabb94
f68d4c
f37022

Requirements
Must have
• cartloom function or booking button function
Nice to have
• Would like to be able to easily move photos change wording and have a sliding photo's function in the website header

```html
<!DOCTYPE html>
<html lang="en">
<head>
<meta charset="utf-8">
<title>Harrowgate Lodge – Boutique Bed &amp; Breakfast</title>
<link href="https://fonts.googleapis.com/css2?family=Playfair+Display:wght@400;700;900&family=Open+Sans:wght@400;600;700&display=swap" rel="stylesheet">
<style>
:root{
  --teal:#33b8a4;
  --teal-dark:#00a990;
  --orange:#f37022;
  --orange-mid:#f68d4c;
  --orange-deep:#e0601a;
  --ice:#ecf7fb;
  --sky:#cee9f5;
  --ink:#1f1f1f;
  --grey:#6f6f6f;
  --white:#ffffff;
}
*{box-sizing:border-box;margin:0;padding:0}
html,body{width:1200px;height:2773px;overflow:hidden;background:var(--white)}
body{position:relative;font-family:'Open Sans',sans-serif;color:var(--ink)}
.serif{font-family:'Playfair Display',serif}
.abs{position:absolute}
.photo{position:absolute;display:block}

/* header */
.site-header{position:absolute;left:0;top:0;width:1200px;height:100px;background:var(--white)}
.social{position:absolute;display:flex;gap:8px}
.social span{width:22px;height:22px;border-radius:50%;background:var(--ice);display:block}
.social span.on{background:var(--orange)}
.brand{position:absolute;left:496px;top:20px;width:210px;height:64px;border:3px solid var(--teal);border-radius:14px;display:flex;align-items:center;justify-content:center;font-family:'Playfair Display',serif;font-weight:700;font-size:17px;color:var(--teal);letter-spacing:.5px;text-transform:uppercase;white-space:nowrap}
.tools{position:absolute;left:876px;top:42px;display:flex;gap:12px}
.nav{position:absolute;left:0;top:100px;width:1200px;height:35px;background:var(--teal);display:flex;justify-content:center;align-items:center;gap:28px}
.nav a{color:var(--white);text-decoration:none;font-family:'Playfair Display',serif;font-size:12px}

/* hero */
.hero{position:absolute;left:0;top:135px;width:1200px;height:427px;background:linear-gradient(90deg,#dfeef2,#eef6f8)}
.hero-side{position:absolute;left:880px;top:0;width:320px;height:427px;background:linear-gradient(160deg,#e96a28,var(--orange) 50%,#d9581a)}
.hero-photo{left:303px;top:37px;width:649px;height:359px;background:linear-gradient(135deg,#6c4a3a,#a7523a 40%,#c9a27a 65%,#556b4a)}
.hero-title{position:absolute;left:125px;top:135px;line-height:1;z-index:2}
.hero-title .l1{font-family:'Playfair Display',serif;font-weight:900;font-size:50px;color:var(--ink)}
.hero-title .l2{font-family:'Playfair Display',serif;font-weight:700;font-size:28px;margin-top:6px}
.hero-title .l2 b{color:var(--orange)}
.hero-title .l3{font-family:'Playfair Display',serif;font-weight:700;font-size:48px;color:var(--orange);margin-top:4px}
.btn{position:absolute;display:flex;align-items:center;justify-content:center;color:var(--white);font-family:'Playfair Display',serif;font-size:12px;z-index:2}
.btn.teal{background:var(--teal)}
.btn.orange{background:var(--orange)}

/* section headings */
.h-orange{font-family:'Playfair Display',serif;font-weight:700;color:var(--orange);text-transform:uppercase}
.h-dark{font-family:'Playfair Display',serif;font-weight:700;color:var(--ink)}
.center{text-align:center;width:1200px;left:0}

.small{font-size:10px;line-height:16px;color:var(--ink)}
.card-label{position:absolute;color:var(--white)}
.card-label .t{font-family:'Playfair Display',serif;font-weight:700;font-size:38px;line-height:1}
.card-label .s{font-family:'Playfair Display',serif;font-size:11px;margin-top:4px}

.offer-title{font-family:'Playfair Display',serif;font-size:15px;color:var(--ink)}
.offer-text{font-size:9.5px;line-height:15px;color:var(--grey);margin-top:6px}
.offer-link{font-family:'Playfair Display',serif;font-weight:700;font-size:11px;color:var(--orange);margin-top:6px}

.about{position:absolute;left:0;top:2158px;width:1200px;height:279px;background:var(--ice)}

/* footer */
.footer{position:absolute;left:0;top:2437px;width:1200px;height:296px;background:var(--orange)}
.footer-bar{position:absolute;left:0;top:2733px;width:1200px;height:40px;background:var(--orange-deep);color:var(--white);font-size:9px;display:flex;align-items:center;justify-content:center}
.f-col{position:absolute;top:60px;color:var(--white)}
.f-col h4{font-family:'Playfair Display',serif;font-weight:700;font-size:15px;margin-bottom:18px}
.f-col p{font-size:9.5px;line-height:15px}
.f-col li{list-style:none;font-size:9.5px;margin-bottom:8.5px;padding-left:16px;position:relative}
.f-col li::before{content:"";position:absolute;left:0;top:3px;border-left:5px solid var(--white);border-top:3.5px solid transparent;border-bottom:3.5px solid transparent}
.gallery{display:grid;grid-template-columns:repeat(3,52px);gap:6px}
.gallery span{height:44px;background:linear-gradient(135deg,#6a5448,#b29a86);border:1px solid rgba(255,255,255,.6)}
</style>
</head>
<body>

<header class="site-header">
  <div class="social" style="left:252px;top:39px" aria-label="Social links">
    <span></span><span class="on"></span><span></span><span></span>
  </div>
  <div class="brand">Harrowgate Lodge</div>
  <div class="tools" aria-label="Search, account and cart">
    <svg width="16" height="16" viewBox="0 0 16 16"><circle cx="6.5" cy="6.5" r="4.5" fill="none" stroke="#222" stroke-width="2"/><line x1="10" y1="10" x2="14.5" y2="14.5" stroke="#222" stroke-width="2"/></svg>
    <svg width="16" height="16" viewBox="0 0 16 16"><circle cx="8" cy="5" r="3.3" fill="none" stroke="#222" stroke-width="1.8"/><path d="M2 15c0-4 3-5.5 6-5.5s6 1.5 6 5.5" fill="none" stroke="#222" stroke-width="1.8"/></svg>
    <svg width="18" height="18" viewBox="0 0 18 18"><path d="M3 5h10l-1 10H4z" fill="none" stroke="#222" stroke-width="1.8"/><path d="M6 5V3.5a2 2 0 0 1 4 0V5" fill="none" stroke="#222" stroke-width="1.5"/><circle cx="14" cy="14" r="3.5" fill="var(--orange)"/></svg>
  </div>
</header>

<nav class="nav">
  <a>Home</a><a>About us</a><a>Booking</a><a>Packages</a><a>Gallery</a><a>Things To Do</a><a>Contact us</a>
</nav>

<section class="hero">
  <div class="hero-side"></div>
  <div class="photo hero-photo" role="img" aria-label="Vintage double-decker bus parked outside the red brick inn"></div>
  <svg class="abs" style="left:893px;top:190px" width="24" height="40" viewBox="0 0 24 40"><path d="M20 4 4 20l16 16" fill="none" stroke="#fff" stroke-width="2.5"/></svg>
  <svg class="abs" style="left:975px;top:190px" width="24" height="40" viewBox="0 0 24 40"><path d="M4 4l16 16L4 36" fill="none" stroke="#fff" stroke-width="2.5"/></svg>
  <div class="hero-title">
    <div class="l1">TAKINGS</div>
    <div class="l2"><b>BOOKING</b> NOW</div>
    <div class="l3">2019</div>
  </div>
  <div class="btn teal" style="left:125px;top:283px;width:110px;height:33px">Book Now</div>
</section>

<h2 class="abs center h-orange" style="top:600px;font-size:31px">Accommodation</h2>
<h3 class="abs center h-dark" style="top:640px;font-size:22px">Special Offers</h3>

<div class="photo" style="left:144px;top:712px;width:457px;height:384px;background:linear-gradient(135deg,#8a2c1a,#b5452a 45%,#c98d6a 70%,#7a4a36)" role="img" aria-label="Red sitting room with armchair, sofa and fireplace"></div>
<p class="abs small" style="left:144px;top:1114px">Make sure you keep up to date with our latest Specials.<br>Click on our Packages link for more details</p>
<p class="abs serif" style="left:144px;top:1157px;font-size:11px;font-weight:700">Our Packages</p>
<div class="photo" style="left:688px;top:760px;width:362px;height:405px;background:linear-gradient(180deg,#3e3b38,#6b6560 35%,#c88a3a 70%,#5a3a1a)" role="img" aria-label="Paddle steamer lit up on the river at dusk"></div>

<div class="photo" style="left:24px;top:1231px;width:784px;height:354px;background:linear-gradient(180deg,#c9c6c0,#8c8a78 45%,#5a5a48 80%,#3a3a32)" role="img" aria-label="Heritage building with trees and vintage car"></div>
<div class="card-label" style="left:52px;top:1494px"><div class="t">P. S. MARINER</div><div class="s">Book Now</div></div>
<div class="photo" style="left:856px;top:1231px;width:344px;height:354px;background:linear-gradient(135deg,#6c4a3a,#a7523a 45%,#c9a27a 70%,#3a2a22)" role="img" aria-label="Vintage double-decker bus beside the inn"></div>
<div class="card-label" style="left:880px;top:1505px"><div class="t">12 ON HARE</div><div class="s">Book Now</div></div>

<h2 class="abs h-orange" style="left:113px;top:1773px;font-size:28px">Special Offers</h2>
<p class="abs serif" style="left:115px;top:1815px;font-size:19px;line-height:26px;color:#444">Make sure you keep up to date<br>with our latest Specials.</p>
<div class="btn orange" style="left:116px;top:1880px;width:111px;height:32px">Book Now</div>

<div class="photo" style="left:416px;top:1659px;width:228px;height:366px;background:linear-gradient(160deg,#a23e22,#7a3220 40%,#c28a6c 75%,#8a5a44)" role="img" aria-label="Guest room with fireplace and upholstered chairs"></div>
<div class="abs" style="left:416px;top:2034px;width:230px">
  <div class="offer-title">Harrowgate Lodge</div>
  <div class="offer-text">Originally built in the early 1870's however back then it was known as The Harrowgate Hotel.</div>
  <div class="offer-link">Book Now</div>
</div>
<div class="photo" style="left:671px;top:1659px;width:228px;height:227px;background:linear-gradient(180deg,#3e3b38,#6b6560 35%,#c88a3a 70%,#5a3a1a)" role="img" aria-label="Paddle steamer on the river"></div>
<div class="abs" style="left:671px;top:1899px;width:230px">
  <div class="offer-title">P. S. Mariner</div>
  <div class="offer-text">Built in Riverbend in 1874 the Mariner has had a long and chequered life working on the river</div>
  <div class="offer-link">Book Now</div>
</div>
<div class="photo" style="left:925px;top:1659px;width:229px;height:227px;background:linear-gradient(180deg,#c9c6c0,#8c8a78 50%,#5a4a3a)" role="img" aria-label="Heritage cottage with vintage car out front"></div>
<div class="abs" style="left:925px;top:1899px;width:230px">
  <div class="offer-title">12 on Hare</div>
  <div class="offer-text">Our heritage listed tastefully restored, fully self contained miners cottage offering superb</div>
  <div class="offer-link">Book Now</div>
</div>

<section class="about">
  <h2 class="abs center h-dark" style="top:48px;font-size:30px">ABOUT US</h2>
  <p class="abs" style="left:305px;top:104px;width:590px;text-align:center;font-size:11px;line-height:18px;color:var(--grey)">The Harrowgate Lodge was originally built in the early 1870's however back then it was known as The Harrowgate Hotel, a very popular watering hole with rivermen and stevedores due to its close proximity to the wharf.Today it is a Heritage Register listed unique boutique Bed &amp; Breakfast which can accommodate up to 24 guests including children, yes we are child friendly.</p>
  <div class="btn teal" style="left:545px;top:196px;width:111px;height:33px">Read More</div>
</section>

<footer class="footer">
  <div class="f-col" style="left:250px">
    <h4>Contact Us</h4>
    <p>Harrowgate Lodge Riverbend<br><br>12 River Terrace, Riverbend, 3999<br><br>Tel: (03) 5400 1234<br><br>Fax: (03) 5400 1235<br><br>stay@harrowgatelodge.com.au</p>
    <div class="social" style="position:relative;margin-top:14px" aria-label="Social links">
      <span style="background:var(--orange-deep)"></span><span style="background:var(--orange-deep)"></span><span style="background:var(--orange-deep)"></span><span style="background:var(--orange-deep)"></span>
    </div>
  </div>
  <div class="f-col" style="left:442px">
    <h4>Quick Links</h4>
    <ul><li>Home</li><li>About Us</li><li>Booking</li><li>Packages</li><li>Gallery</li><li>Things To Do</li><li>Contact Us</li></ul>
  </div>
  <div class="f-col" style="left:560px;width:190px">
    <h4>Our History</h4>
    <p>The Harrowgate Lodge was originally built in the early 1870's however back then it was known as The Harrowgate Hotel, a very popular watering hole with rivermen and stevedores due to its close proximity to the wharf.Today it is a Heritage Register listed unique boutique Bed &amp; Breakfast which can accommodate u</p>
  </div>
  <div class="f-col" style="left:778px">
    <h4>Gallery</h4>
    <div class="gallery" role="img" aria-label="Gallery thumbnails of rooms, guests and the river">
      <span></span><span></span><span></span><span></span><span></span><span></span><span></span><span></span><span></span>
    </div>
  </div>
</footer>
<div class="footer-bar">Copyright © 2019&nbsp;<b>Harrowgate Lodge.</b>&nbsp;Powered by NORTHBANK WEB</div>

</body>
</html>
```